Roofing Trade Show - Retractable Banners

We need retractable banners to go beside our table for trade shows and markets. One banner will focus on Homeowners and the other banner will target Commercial Property Managers. We provide roof installation and repairs on several roof types for residential and commercial properties. Our logo color is Teal.
There are 2 Design Guideline files attached but we are open to your artistic design suggestions.
Also included here along are some logo varions and some residential roof images.
We don't have any commercial / industrial rooftop images so royalty free stock photos are fine.
If you have questions, please contact me.
Target Market(s)
Commercial Property Managers and Real Estate Brokers
Industry/Entity Type
Construction
Look and feel

```html
<!DOCTYPE html>
<html lang="en">
<head>
<meta charset="utf-8">
<title>Cove Point Roofing – Commercial Trade Show Banner</title>
<link href="https://fonts.googleapis.com/css2?family=Bebas+Neue&family=Montserrat:wght@600;700;800&family=Poppins:wght@400;500&display=swap" rel="stylesheet">
<style>
  :root {
    --backdrop: #2a2a2a;
    --paper: #f4f4f4;
    --panel: #f0f0f0;
    --teal: #0b8e96;
    --teal-band: #21958b;
    --teal-text: #12898f;
    --ink: #1c1c1c;
    --grey-text: #3a3a3a;
    --white: #ffffff;
  }
  * { box-sizing: border-box; margin: 0; padding: 0; }
  html, body { width: 1200px; height: 1200px; overflow: hidden; background: var(--backdrop); }
  .banner { position: absolute; left: 352px; top: 0; width: 497px; height: 1200px; background: var(--paper); overflow: hidden; font-family: "Poppins", sans-serif; }
  .abs { position: absolute; }

  .brand { left: 39px; top: 50px; display: flex; align-items: center; gap: 10px; }
  .brand-square { width: 44px; height: 44px; background: var(--teal-text); }
  .brand-name { font-family: "Montserrat", sans-serif; font-weight: 700; color: var(--teal-text); font-size: 19px; line-height: 1.1; letter-spacing: .5px; }

  .contact { right: 37px; top: 54px; text-align: right; }
  .contact-phone { font-family: "Montserrat", sans-serif; font-weight: 700; color: var(--teal-text); font-size: 22px; line-height: 1; }
  .contact-web { font-family: "Montserrat", sans-serif; font-weight: 600; color: var(--grey-text); font-size: 11.5px; letter-spacing: .6px; margin-top: 6px; }

  .top-accent { left: 255px; top: 129px; width: 242px; height: 13px; background: var(--teal); }

  .hero-photo { left: 0; top: 142px; width: 497px; height: 296px; background: linear-gradient(180deg, #a9a3c4 0%, #c8a8b6 30%, #6b6f86 55%, #5d6272 80%, #6f7460 100%); }
  .hero-band { left: 0; top: 343px; width: 432px; height: 146px; background: var(--teal); opacity: .96; }
  .hero-title { left: 45px; top: 365px; font-family: "Montserrat", sans-serif; font-weight: 800; color: var(--white); font-size: 27px; line-height: 31.5px; letter-spacing: 1.2px; }

  .audience { left: 45px; top: 518px; font-family: "Bebas Neue", sans-serif; color: var(--ink); font-size: 40px; line-height: 37.5px; }
  .audience-rule { left: 45px; top: 637px; width: 201px; height: 2px; background: var(--ink); }
  .types-title { left: 45px; top: 652px; font-family: "Montserrat", sans-serif; font-weight: 700; color: var(--ink); font-size: 21px; }
  .types-list { top: 683px; list-style: none; font-family: "Montserrat", sans-serif; font-weight: 600; color: var(--ink); font-size: 14px; line-height: 21px; }
  .types-list li::before { content: ""; display: inline-block; width: 8px; height: 8px; border: 1.6px solid var(--ink); border-radius: 50%; margin-right: 5px; vertical-align: 1px; }
  .types-left { left: 46px; }
  .types-right { left: 178px; }

  .frame-top { left: 370px; top: 502px; width: 88px; height: 79px; background: var(--teal-band); }
  .frame-bottom { left: 304px; top: 676px; width: 88px; height: 78px; background: var(--teal-band); }
  .photo-tile-roof { left: 319px; top: 517px; width: 124px; height: 109px; background: linear-gradient(160deg, #e6e8ea 0%, #d89a72 45%, #c98a3e 100%); }
  .photo-tile-slate { left: 318px; top: 632px; width: 124px; height: 109px; background: linear-gradient(160deg, #8aa07a 0%, #6a6c70 35%, #4a4c50 100%); }

  .services { left: 0; top: 770px; width: 497px; height: 334px; background: var(--teal-band); }
  .service-icon { left: 44px; width: 61px; height: 61px; background: var(--white); display: flex; align-items: center; justify-content: center; }
  .service { left: 126px; width: 334px; color: var(--white); }
  .service-title { font-family: "Montserrat", sans-serif; font-weight: 700; font-size: 15px; letter-spacing: .4px; line-height: 18px; }
  .service-text { font-size: 7.9px; line-height: 9.2px; letter-spacing: .35px; margin-top: 2px; }

  .cta { left: 38px; top: 1124px; width: 422px; font-family: "Bebas Neue", sans-serif; font-size: 31.5px; line-height: 1; white-space: nowrap; color: var(--ink); }
  .cta-accent { color: var(--teal-text); }
  .license { left: 38px; top: 1153px; width: 422px; text-align: right; white-space: nowrap; font-size: 13.4px; color: var(--teal-text); }
  .license strong { font-weight: 500; }
  .bottom-strip { left: 0; top: 1191px; width: 497px; height: 9px; background: var(--teal-band); }
</style>
</head>
<body>
<main class="banner">
  <div class="abs brand">
    <span class="brand-square"></span>
    <span class="brand-name">COVE POINT<br>ROOFING</span>
  </div>
  <div class="abs contact">
    <div class="contact-phone">(555) 214-0190</div>
    <div class="contact-web">WWW.COVEPOINTROOFING.COM</div>
  </div>

  <div class="abs top-accent"></div>
  <div class="abs hero-photo" role="img" aria-label="Two-storey house with dark shingle roof at dusk"></div>
  <div class="abs hero-band"></div>
  <h1 class="abs hero-title">COMMERCIAL ROOFING<br>THAT PROTECTS YOUR<br>INVESTMENT</h1>

  <h2 class="abs audience">SERVING PROPERTY<br>MANAGERS &amp;<br>REALTORS ACROSS</h2>
  <div class="abs audience-rule"></div>
  <h3 class="abs types-title">ROOF TYPES:</h3>
  <ul class="abs types-list types-left"><li>FLAT ROOFS</li><li>LOW-SLOPE</li><li>TPO</li></ul>
  <ul class="abs types-list types-right"><li>PVC</li><li>BUILT-UP</li><li>COATINGS</li></ul>

  <div class="abs frame-top"></div>
  <div class="abs frame-bottom"></div>
  <div class="abs photo-tile-roof" role="img" aria-label="Terracotta tile roofs over brick walls"></div>
  <div class="abs photo-tile-slate" role="img" aria-label="Dark grey tile roof with skylight"></div>

  <section class="abs services">
    <div class="abs service-icon" style="top:31px">
      <svg width="40" height="40" viewBox="0 0 40 40" fill="none" stroke="#111" stroke-width="2.2" stroke-linecap="round"><circle cx="15" cy="15" r="10"/><path d="M10 15l4 4 7-8"/><path d="M23 23l11 11" stroke-width="4"/></svg>
    </div>
    <div class="abs service" style="top:33px">
      <div class="service-title">INSPECTIONS</div>
      <p class="service-text">Our thorough roof inspections help identify potential issues before they become costly problems. We assess the overall condition of your roof, checking for leaks, damaged shingles, and structural weaknesses to ensure your home stays secure year-round.</p>
    </div>

    <div class="abs service-icon" style="top:103px">
      <svg width="40" height="40" viewBox="0 0 40 40" fill="none" stroke="#111" stroke-width="1.8" stroke-linejoin="round"><path d="M3 20L20 5l17 15"/><path d="M8 16v20h24V16"/><path d="M16 36V26h8v10"/><path d="M21 8l-3 6 4 2-3 6"/></svg>
    </div>
    <div class="abs service" style="top:106px">
      <div class="service-title">LEAK REPAIR</div>
      <p class="service-text">Water intrusion can lead to significant damage if left untreated. Our expert team quickly locates and repairs leaks, preventing further structural harm and maintaining the integrity of your roof.</p>
    </div>

    <div class="abs service-icon" style="top:175px">
      <svg width="44" height="40" viewBox="0 0 44 40" fill="none" stroke="#111" stroke-width="1.6" stroke-linejoin="round"><path d="M2 30L20 12l18 18z"/><path d="M8 24h24M13 19h14"/><circle cx="34" cy="10" r="7"/><path d="M31 10h6M34 7v6"/></svg>
    </div>
    <div class="abs service" style="top:177px">
      <div class="service-title">RE-ROOFING</div>
      <p class="service-text">When repairs are no longer sufficient, we offer professional re-roofing services. Whether you're upgrading materials or replacing an aging roof, we provide durable, high-quality solutions designed to protect your home for years to come.</p>
    </div>

    <div class="abs service-icon" style="top:247px">
      <svg width="36" height="40" viewBox="0 0 36 40" fill="none" stroke="#111" stroke-width="1.6"><rect x="4" y="6" width="22" height="30"/><rect x="9" y="3" width="22" height="30" fill="#fff"/><circle cx="20" cy="11" r="3"/><path d="M13 19h14M13 23h14M13 27h10"/></svg>
    </div>
    <div class="abs service" style="top:249px">
      <div class="service-title">MAINTENANCE PLANS</div>
      <p class="service-text">Regular maintenance is key to extending the life of your roof. Our tailored maintenance plans include routine inspections, cleaning, and preventative repairs—helping you avoid unexpected costs and ensuring your roof performs at its best.</p>
    </div>
  </section>

  <p class="abs cta">CALL TODAY <span class="cta-accent">FOR A FREE ROOF HEALTH CHECK</span></p>
  <p class="abs license"><strong>Cove Point Roofing</strong>, Inc. C-39 Roofing Contractor Lic. #1048213</p>
  <div class="abs bottom-strip"></div>
</main>
</body>
</html>
```